New Business Card Design Project

hello again,
i have an awful year and we were not able to complete our logo plan. we would like to use our #1 logo for business card design process. the primary colors for business card should be white background with orange & black letters. our business is mobil truck cranes. we deliver heavy stuff and unload cargo with crane that is mounted on our trucks.
here is our business card info:
HARBOR LIFT HAULERS, INC.
428 WESTCOTT AVE
MERRICK, NY 11542
OFFICE - 516 487 3091
DIRECT - 1 888 LIFT HAULS
MARK@HLHAULERS.COM
PLEASE also try to get our slogan on card .... "Our Loads Keep Rollin"
lastly please also put "24 hour Knuckleboom Service"
you can call me anytime 24/7 to discuss...my cell # is: 516 759 2036
please also list: Mark Delroy, President
Target Market(s)
Heavy Construction industry
Industry/Entity Type
heavy construction industry
Contact Information for Business Card
24 Hr Knuckleboom Service

```html
<!DOCTYPE html>
<html lang="en">
<head>
<meta charset="utf-8">
<title>Harbor Lift Haulers – Business Card</title>
<link rel="stylesheet" href="https://fonts.googleapis.com/css2?family=Montserrat:wght@400;500;700;800&display=swap">
<style>
  :root {
    --orange: #f53000;
    --ink: #2e2e2e;
    --paper: #ffffff;
    --backdrop: #e4e4e4;
    --art-light: #d9d9d9;
    --art-dark: #444444;
  }
  * { box-sizing: border-box; margin: 0; padding: 0; }
  html, body { width: 1200px; height: 1015px; overflow: hidden; }
  body {
    background: var(--backdrop);
    font-family: "Montserrat", sans-serif;
    color: var(--ink);
    position: relative;
  }
  .card {
    position: absolute;
    left: 170px;
    width: 860px;
    height: 480px;
    background: var(--paper);
    overflow: hidden;
    box-shadow: 0 6px 18px rgba(0,0,0,0.18);
  }
  .card--front { top: 18px; }
  .card--back { top: 517px; }

  /* Front */
  .brand {
    position: absolute;
    top: 110px; left: 0; right: 0;
    text-align: center;
  }
  .brand__slogan {
    font-weight: 700;
    font-size: 22px;
    letter-spacing: 3px;
    color: var(--ink);
    margin-bottom: 18px;
  }
  .brand__name {
    display: inline-flex;
    align-items: center;
    gap: 18px;
    font-weight: 800;
    font-size: 46px;
    letter-spacing: 1px;
    color: var(--ink);
  }
  .brand__dot {
    width: 30px; height: 30px;
    border-radius: 50%;
    background: var(--orange);
    flex: none;
  }
  .service-band {
    position: absolute;
    left: 0; right: 0; bottom: 0;
    height: 108px;
    background: var(--orange);
    display: flex;
    align-items: center;
    justify-content: center;
    color: var(--paper);
    font-weight: 500;
    font-size: 25px;
    letter-spacing: 1.5px;
  }

  /* Back */
  .accent-block {
    position: absolute;
    left: 38px; top: 110px;
    width: 46px; height: 70px;
    background: var(--orange);
  }
  .person {
    position: absolute;
    left: 108px; top: 102px;
  }
  .person__name {
    font-weight: 800;
    font-size: 40px;
    color: var(--orange);
    line-height: 1;
    white-space: nowrap;
  }
  .person__role {
    font-weight: 500;
    font-size: 19px;
    letter-spacing: 0.5px;
    margin-top: 6px;
  }
  .contacts {
    position: absolute;
    left: 108px; top: 206px;
    list-style: none;
  }
  .contacts li {
    display: flex;
    align-items: center;
    gap: 12px;
    font-size: 19px;
    font-weight: 500;
    height: 31px;
    white-space: nowrap;
  }
  .contacts svg { width: 24px; height: 24px; flex: none; }
  .hl { color: var(--orange); }
  .address {
    position: absolute;
    left: 108px; top: 355px;
    font-size: 19px;
    font-weight: 500;
    line-height: 1.35;
  }
  .address__company { color: var(--orange); font-weight: 700; }
  .truck-art {
    position: absolute;
    right: 0; top: 60px;
    width: 330px; height: 420px;
    background: linear-gradient(160deg, var(--art-light), var(--art-dark));
  }
</style>
</head>
<body>

<section class="card card--front">
  <div class="brand">
    <p class="brand__slogan">OUR LOADS KEEP ROLLIN</p>
    <p class="brand__name"><span class="brand__dot"></span>HARBOR LIFT HAULERS INC</p>
  </div>
  <div class="service-band">24 HOUR KNUCKLEBOOM SERVICE</div>
</section>

<section class="card card--back">
  <div class="accent-block"></div>
  <div class="person">
    <p class="person__name">MARK DELROY</p>
    <p class="person__role">PRESIDENT</p>
  </div>
  <ul class="contacts">
    <li>
      <svg viewBox="0 0 24 24"><circle cx="12" cy="12" r="12" fill="var(--orange)"/><path d="M8 6.5l2 0 1 3-1.4 1.2a8 8 0 0 0 3.7 3.7L14.5 13l3 1v2a1.5 1.5 0 0 1-1.6 1.5A10 10 0 0 1 6.5 8.1 1.5 1.5 0 0 1 8 6.5z" fill="#fff"/></svg>
      516 487 3091
    </li>
    <li>
      <svg viewBox="0 0 24 24"><circle cx="12" cy="12" r="12" fill="var(--orange)"/><path d="M8 6.5l2 0 1 3-1.4 1.2a8 8 0 0 0 3.7 3.7L14.5 13l3 1v2a1.5 1.5 0 0 1-1.6 1.5A10 10 0 0 1 6.5 8.1 1.5 1.5 0 0 1 8 6.5z" fill="#fff"/></svg>
      <span>1 888 LIFT HAULS <span class="hl">(DIRECT)</span></span>
    </li>
    <li>
      <svg viewBox="0 0 24 24"><circle cx="12" cy="12" r="12" fill="var(--orange)"/><rect x="6" y="8" width="12" height="8.5" fill="#fff"/><path d="M6 8l6 5 6-5" fill="none" stroke="var(--orange)" stroke-width="1.3"/></svg>
      MARK@HLHAULERS.COM
    </li>
    <li>
      <svg viewBox="0 0 24 24"><circle cx="12" cy="12" r="12" fill="var(--orange)"/><g fill="none" stroke="#fff" stroke-width="1.3"><circle cx="12" cy="12" r="6"/><ellipse cx="12" cy="12" rx="2.6" ry="6"/><path d="M6 12h12M7 9h10M7 15h10"/></g></svg>
      <span>WWW.<span class="hl">HLHAULERS</span>.COM</span>
    </li>
  </ul>
  <div class="address">
    <p class="address__company">HARBOR LIFT HAULERS, INC.</p>
    <p>428 WESTCOTT AVE</p>
    <p>MERRICK, NY 11542</p>
  </div>
  <div class="truck-art" role="img" aria-label="Large crane truck illustration in dark grey with orange wheel hubs"></div>
</section>

</body>
</html>
```